Design a For Sale sign board and Direction Sign Board.
Attached is an example of what i am thinking but am happy to look at any options.
Colours are to be ""bright Orange"on white and in reverse as well.

Logo id Fairbrook & Co Real Estate.

```html
<!DOCTYPE html>
<html lang="en">
<head>
<meta charset="utf-8">
<title>Fairbrook &amp; Co Real Estate – Sale and Direction Signs</title>
<link rel="stylesheet" href="https://fonts.googleapis.com/css2?family=Comfortaa:wght@500;700&display=swap">
<style>
  :root {
    --backdrop: #c1c1c1;
    --brand-orange: #f6961f;
    --board-white: #ffffff;
  }
  * { box-sizing: border-box; margin: 0; padding: 0; }
  html, body {
    width: 1000px;
    height: 1200px;
    overflow: hidden;
    background: var(--backdrop);
  }
  .canvas {
    position: relative;
    width: 1000px;
    height: 1200px;
  }
  .sign {
    position: absolute;
    left: 210px;
    width: 580px;
    height: 411px;
    display: flex;
    flex-direction: column;
  }
  .sign--sale { top: 165px; }
  .sign--direction { top: 624px; }

  .sign__brand {
    height: 205px;
    background: var(--board-white);
    display: flex;
    flex-direction: column;
    align-items: center;
    justify-content: center;
    color: var(--brand-orange);
    font-family: "Comfortaa", sans-serif;
    font-weight: 700;
  }
  .brand-name {
    font-size: 54px;
    line-height: 1;
    letter-spacing: -1px;
  }
  .brand-tagline {
    font-size: 30px;
    line-height: 1;
    margin-top: 12px;
    align-self: flex-end;
    margin-right: 126px;
  }

  .sign__contact {
    flex: 1;
    background: var(--brand-orange);
    color: var(--board-white);
    font-family: "Comfortaa", sans-serif;
    display: flex;
    flex-direction: column;
    align-items: center;
  }
  .agent-name {
    font-weight: 500;
    font-size: 42px;
    line-height: 1;
    margin-top: 32px;
  }
  .agent-phone {
    font-weight: 700;
    font-size: 76px;
    line-height: 1;
    margin-top: 18px;
    letter-spacing: -2px;
  }
  .direction-arrow {
    margin-top: 22px;
    width: 376px;
    height: 62px;
  }
</style>
</head>
<body>
<main class="canvas">
  <section class="sign sign--sale" aria-label="For sale sign board">
    <header class="sign__brand">
      <span class="brand-name">Fairbrook &amp; Co</span>
      <span class="brand-tagline">Real Estate</span>
    </header>
    <div class="sign__contact">
      <p class="agent-name">Daniel Hart</p>
      <p class="agent-phone">0400 555 127</p>
    </div>
  </section>

  <section class="sign sign--direction" aria-label="Direction sign board">
    <header class="sign__brand">
      <span class="brand-name">Fairbrook &amp; Co</span>
      <span class="brand-tagline">Real Estate</span>
    </header>
    <div class="sign__contact">
      <p class="agent-name">Daniel Hart</p>
      <svg class="direction-arrow" viewBox="0 0 376 62" role="img" aria-label="Arrow pointing left">
        <polygon fill="var(--board-white)"
          points="0,31 40,0 70,0 36,21 376,21 376,41 36,41 70,62 40,62"/>
      </svg>
    </div>
  </section>
</main>
</body>
</html>
```